Korvex Systems*

Stationary design including business cards, letter heads, envelops and email signatures using our new logo

Target Market(s)

Innovative Technologies

Industry/Entity Type

Defense Contracting

Font styles to use
Sans Serif

```html
<!DOCTYPE html>
<html lang="en">
<head>
<meta charset="utf-8">
<title>Korvex Systems Letterhead</title>
<link href="https://fonts.googleapis.com/css2?family=Open+Sans:wght@400;600&family=Roboto:wght@400;500&display=swap" rel="stylesheet">
<style>
  :root {
    --backdrop: #dedede;
    --paper: #fbfbfb;
    --ink: #111111;
    --body-text: #4a4a4a;
    --footer-text: #333333;
    --band: #0a0a0a;
    --signature-tone: #e4e4e4;
  }
  * { margin: 0; padding: 0; box-sizing: border-box; }
  html, body {
    width: 1200px;
    height: 800px;
    overflow: hidden;
    background: var(--backdrop);
  }
  .letterhead {
    position: absolute;
    left: 324px;
    top: 15px;
    width: 552px;
    height: 770px;
    background: var(--paper);
    font-family: "Open Sans", sans-serif;
    color: var(--body-text);
  }
  .brand-name {
    position: absolute;
    left: 50px;
    top: 104px;
    font-family: "Open Sans", sans-serif;
    font-weight: 600;
    font-size: 17px;
    letter-spacing: 0.5px;
    text-transform: uppercase;
    color: var(--ink);
  }
  .letter-body {
    position: absolute;
    left: 50px;
    top: 178px;
    width: 452px;
    font-size: 10.2px;
    line-height: 14.9px;
  }
  .salutation { margin-bottom: 15px; }
  .letter-body .paragraph {
    text-align: justify;
    margin-bottom: 15px;
  }
  .closing { margin-top: 29px; }
  .signature-area {
    position: absolute;
    left: 50px;
    top: 660px;
    width: 66px;
    height: 62px;
  }
  .signature-area {
    top: 528px;
  }
  .footer-contact {
    position: absolute;
    left: 50px;
    top: 701px;
    display: flex;
    gap: 16px;
    font-family: "Roboto", sans-serif;
    font-size: 10.4px;
    line-height: 13.6px;
    color: var(--footer-text);
  }
  .contact-line { display: flex; align-items: center; gap: 3px; }
  .contact-line svg { width: 9px; height: 9px; flex: none; }
  .company-name { font-weight: 500; color: var(--ink); }
  .footer-band {
    position: absolute;
    left: 0;
    bottom: 0;
    width: 100%;
    height: 13px;
    background: var(--band);
  }
</style>
</head>
<body>
  <main class="letterhead">
    <div class="brand-name">Korvex Systems</div>

    <section class="letter-body">
      <p class="salutation">Dear customer,</p>
      <p class="paragraph">Lorem ipsum dolor sit amet, consectetur adipisicing elit, sed do eiusmod tempor incididunt ut labore et dolore magna aliqua. Ut enim ad minim veniam, quis nostrud exercitation ullamco laboris nisi ut aliquip ex ea commodo consequat. Duis aute irure dolor in reprehenderit in voluptate velit esse cillum dolore eu fugiat nulla pariatur. Excepteur sint occaecat cupidatat non proident, sunt in culpa qui officia deserunt mollit anim id est laborum.</p>
      <p class="paragraph">Lorem ipsum dolor sit amet, consectetur adipisicing elit, sed do eiusmod tempor incididunt ut labore et dolore magna aliqua. Ut enim ad minim veniam, quis nostrud exercitation ullamco laboris nisi ut aliquip ex ea commodo consequat. Duis aute irure dolor in reprehenderit in voluptate velit esse cillum dolore eu fugiat nulla pariatur. Excepteur sint occaecat cupidatat non proident, sunt in culpa qui officia deserunt mollit anim id est laborum.</p>
      <p class="paragraph">Lorem ipsum dolor sit amet, consectetur adipisicing elit, sed do eiusmod tempor incididunt ut labore et dolore magna aliqua. Ut enim ad minim veniam, quis nostrud exercitation ullamco laboris nisi ut aliquip ex ea commodo consequat. Duis aute irure dolor in reprehenderit in voluptate velit esse cillum dolore eu fugiat nulla pariatur. Excepteur sint occaecat cupidatat non proident, sunt in culpa qui officia deserunt mollit anim id est laborum.</p>
      <p class="closing">Yours Sincerely,</p>
    </section>

    <svg class="signature-area" role="img" aria-label="Handwritten signature of the sender" viewBox="0 0 66 62">
      <rect width="66" height="62" fill="var(--signature-tone)"/>
    </svg>

    <footer class="footer-contact">
      <div class="contact-column">
        <div class="contact-line">
          <svg viewBox="0 0 10 10" aria-hidden="true"><path d="M1 3.5 C1 2 2.5 1.5 5 1.5 C7.5 1.5 9 2 9 3.5 L7.5 4 L6.8 3 L3.2 3 L2.5 4 Z M2.5 5 L7.5 5 L8.5 8.5 L1.5 8.5 Z" fill="var(--ink)"/></svg>
          <span>555.204.7180</span>
        </div>
        <div class="contact-line">
          <svg viewBox="0 0 10 10" aria-hidden="true"><rect x="0.5" y="2" width="9" height="6.5" fill="var(--ink)"/><path d="M0.8 2.3 L5 5.6 L9.2 2.3" stroke="var(--paper)" stroke-width="0.8" fill="none"/></svg>
          <span>ops@korvexsystems.com</span>
        </div>
        <div class="contact-line">
          <svg viewBox="0 0 10 10" aria-hidden="true"><circle cx="5" cy="5" r="4.3" fill="none" stroke="var(--ink)" stroke-width="1"/><path d="M3 2.5 L5.5 3.5 L4.5 5.5 L6.5 7.5 L5 9" fill="var(--ink)" stroke="var(--ink)" stroke-width="1.2"/></svg>
          <span>www.korvexsystems.com</span>
        </div>
      </div>
      <address class="contact-column" style="font-style: normal;">
        <div class="company-name">Korvex Systems</div>
        <div>412 Alder Bend Road</div>
        <div>Fairview, Oh 45990</div>
      </address>
    </footer>

    <div class="footer-band"></div>
  </main>
</body>
</html>
```